Cover Art for my next album 'Driftcoast'

I want the album cover to look like the picture attached, with ambigram lettering, but instead of a plain white background, I want it to be like a grainy type of canvas tan so it looks like the letters are painted on a canvas, and I want the letters to look like they were painted with watercolor, but still with the rainbow color to them like how it goes progressively through all the colors in the rainbow in each of the letters. I also want the backside of it to be the same type of grainy canvas tan color, with the words "As within, so without" in black letters on a white patch with stitching around the edges so it looks like its stitched onto the background

Target Market(s)

Hip Hop Fans

Font styles to use
Other font styles liked:
• Ambigram Watercolor

Requirements
Must have
• grainy light tanish canvas color background, watercolor ambigram lettering that says 'Driftcoast'. same background with a white patch with black or brown stitching on the edges that says 'As within, So without' on the patch.

```html
<!DOCTYPE html>
<html lang="en">
<head>
<meta charset="UTF-8">
<title>Driftcoast — Back Cover</title>
<link rel="stylesheet" href="https://fonts.googleapis.com/css2?family=Kalam:wght@400&display=swap">
<style>
  :root {
    --canvas-tan: #ebe5d6;
    --canvas-weave-light: rgba(255, 255, 255, 0.28);
    --canvas-weave-dark: rgba(150, 135, 105, 0.12);
    --patch-white: #ececef;
    --patch-shade: rgba(120, 120, 130, 0.08);
    --stitch-grey: #8d8d92;
    --ink-black: #222222;
  }

  html, body {
    margin: 0;
    padding: 0;
    overflow: hidden;
  }

  .cover-back {
    position: relative;
    width: 1200px;
    height: 1200px;
    overflow: hidden;
    background-color: var(--canvas-tan);
    background-image:
      repeating-linear-gradient(45deg, var(--canvas-weave-light) 0 1px, transparent 1px 4px),
      repeating-linear-gradient(-45deg, var(--canvas-weave-dark) 0 1px, transparent 1px 4px);
  }

  .stitched-patch {
    position: absolute;
    left: 200px;
    top: 480px;
    width: 791px;
    height: 193px;
    border-radius: 15px;
    background-color: var(--patch-white);
    background-image:
      repeating-linear-gradient(30deg, var(--patch-shade) 0 1px, transparent 1px 3px),
      repeating-linear-gradient(-60deg, var(--patch-shade) 0 1px, transparent 1px 5px);
    box-shadow: 0 1px 2px rgba(0, 0, 0, 0.18);
  }

  .patch-stitching {
    position: absolute;
    inset: 0;
    width: 100%;
    height: 100%;
  }

  .patch-stitching rect {
    fill: none;
    stroke: var(--stitch-grey);
    stroke-width: 2;
    stroke-dasharray: 12 5;
  }

  .patch-motto {
    position: absolute;
    inset: 0;
    margin: 0;
    display: flex;
    align-items: center;
    justify-content: center;
    font-family: "Kalam", cursive;
    font-size: 66px;
    font-weight: 400;
    color: var(--ink-black);
    letter-spacing: 1px;
    white-space: nowrap;
    padding-top: 6px;
  }
</style>
</head>
<body>
  <main class="cover-back">
    <div class="stitched-patch">
      <svg class="patch-stitching" viewBox="0 0 791 193" aria-hidden="true">
        <rect x="10" y="10" width="771" height="173" rx="10" ry="10"/>
      </svg>
      <p class="patch-motto">As within, so without</p>
    </div>
  </main>
</body>
</html>
```